The amber lantern with an elephant incorporated in the background

Target Market(s)

Real estate

Industry/Entity Type

Real Estate

Contact Information for Business Card

On back on want my name & number
In front I want the business name, "the amber lantern", below to say staging & design

Logo Text

The amber lantern

Font styles to use
Serif

Colors
000000

Requirements
Must have
• I want an elephant behind the writing in gold transperant

```html
<!DOCTYPE html>
<html lang="en">
<head>
<meta charset="utf-8">
<title>The Amber Lantern – Business Card</title>
<link rel="stylesheet" href="https://fonts.googleapis.com/css2?family=Cormorant+Garamond:wght@500;600&display=swap">
<style>
  :root {
    --backdrop: #d4d4d4;
    --card: #ffffff;
    --ink: #1a1a1a;
    --ink-soft: #3a3a3a;
    --gold-light: #e3b94a;
    --gold-mid: #c9972a;
    --gold-dark: #8f6514;
    --shadow: rgba(0, 0, 0, 0.28);
  }
  html, body {
    margin: 0;
    padding: 0;
  }
  body {
    width: 1200px;
    height: 1000px;
    overflow: hidden;
    background: var(--backdrop);
    font-family: "Cormorant Garamond", serif;
    color: var(--ink);
    position: relative;
  }
  .card {
    position: absolute;
    top: 345px;
    width: 520px;
    height: 310px;
    background: var(--card);
    box-shadow: 0 3px 10px var(--shadow);
  }
  .card--front { left: 60px; }
  .card--back { left: 620px; }

  .elephant-art {
    position: absolute;
    left: 202px;
    top: 32px;
    width: 116px;
    height: 112px;
    border-radius: 40% 48% 22% 22% / 46% 50% 18% 18%;
    background: radial-gradient(ellipse at 45% 40%, var(--gold-light), var(--gold-mid) 60%, var(--gold-dark));
  }
  .name-frame {
    position: absolute;
    left: 109px;
    top: 145px;
    width: 297px;
    height: 29px;
    box-sizing: border-box;
    border: 1.5px solid var(--ink);
    display: flex;
    align-items: center;
    justify-content: center;
    font-size: 19px;
    font-weight: 600;
    letter-spacing: 3.5px;
    text-transform: uppercase;
  }
  .contact-line {
    position: absolute;
    left: 0;
    right: 0;
    top: 193px;
    margin: 0;
    text-align: center;
    font-size: 12.5px;
    font-weight: 600;
    letter-spacing: 0.4px;
  }
  .brand-frame {
    position: absolute;
    left: 96px;
    top: 137px;
    width: 328px;
    height: 28px;
    box-sizing: border-box;
    border: 1.5px solid var(--ink);
    display: flex;
    align-items: center;
    justify-content: center;
    font-size: 17px;
    font-weight: 600;
    letter-spacing: 1px;
    text-transform: uppercase;
  }
  .brand-tagline {
    position: absolute;
    left: 0;
    right: 0;
    top: 174px;
    margin: 0;
    text-align: center;
    font-size: 12px;
    font-weight: 500;
    letter-spacing: 3px;
    text-transform: uppercase;
    color: var(--ink-soft);
  }
</style>
</head>
<body>
  <section class="card card--front">
    <div class="elephant-art" role="img" aria-label="Golden ornate elephant figurine with raised trunk"></div>
    <div class="name-frame">Daniel Harper</div>
    <p class="contact-line">000 000 0000 | info@yourmail.com | www.yourweb.com</p>
  </section>

  <section class="card card--back">
    <div class="brand-frame">The Amber Lantern</div>
    <p class="brand-tagline">Staging &amp; Design</p>
  </section>
</body>
</html>
```